Bag packaging design of sliced bread

The project is for design of line of sliced bread with different flavours. The brand of the bread will be "Velorasa". The shape of the bread will be oval. The bread will be packed in a bag. I attach the layout of the bag. The bag will be closed with a plastic clip. I attach images of similar products. The idea is to have one main design and then each colour to be different type of bread like those in the images 2 and 5.

```html
<!DOCTYPE html>
<html lang="ro">
<head>
<meta charset="utf-8">
<title>Velorasa – sliced bread bag line</title>
<link rel="stylesheet" href="https://fonts.googleapis.com/css2?family=Yeseva+One&family=Oswald:wght@400&family=Poppins:wght@600&family=Kaushan+Script&display=swap">
<style>
  :root {
    --cream: #fbf3d3;
    --cream-edge: #f2d6a3;
    --gold: #e8bf4a;
    --gold-light: #f7dc82;
    --gold-text: #f0cf5c;
    --green: #1b5f33;
    --green-glow: #0f8a3e;
    --crimson: #c21d47;
    --crimson-glow: #e01a4d;
    --bread-dark: #c4804d;
    --bread-light: #e3ae78;
    --hanger: #c9c9c9;
    --white: #ffffff;
    --frame: #9a9a9a;
  }
  * { margin: 0; padding: 0; box-sizing: border-box; }
  html, body { width: 1200px; height: 1095px; overflow: hidden; background: var(--white); }
  .canvas {
    position: relative; width: 1200px; height: 1095px;
    border: 1px solid var(--frame); background: var(--white);
  }
  .hanger {
    position: absolute; top: 40px; width: 142px; height: 80px;
    background: var(--hanger); border-radius: 18px 18px 0 0;
  }
  .hanger::after {
    content: ""; position: absolute; left: 51px; top: 10px;
    width: 40px; height: 40px; border-radius: 50%; background: var(--white);
  }
  .hanger--left { left: 223px; }
  .hanger--right { left: 819px; }

  .bag {
    position: absolute; top: 118px; width: 466px; height: 912px;
    overflow: visible;
  }
  .bag--left { left: 62px; --panel: var(--green); --panel-glow: var(--green-glow); }
  .bag--right { left: 658px; --panel: var(--crimson); --panel-glow: var(--crimson-glow); }
  .bag__art { position: absolute; inset: 0; overflow: visible; }

  .bag__text { position: absolute; left: 0; width: 466px; text-align: center; }
  .brand-mark {
    top: 150px; display: flex; justify-content: center; align-items: center; gap: 10px;
    font-family: "Yeseva One", serif; font-size: 34px; color: var(--panel);
  }
  .brand-mark__dot { width: 18px; height: 18px; border-radius: 50%; background: var(--gold); }
  .brand-name {
    top: 478px; font-family: "Yeseva One", serif; font-size: 80px;
    color: var(--white); line-height: 1;
  }
  .variant {
    top: 570px; font-family: "Oswald", sans-serif; font-size: 28px;
    color: var(--gold-text); line-height: 1; letter-spacing: 0.2px;
  }
  .variant__tilde { font-size: 18px; color: var(--gold-light); vertical-align: middle; }
  .claim-top {
    top: 737px; font-family: "Poppins", sans-serif; font-weight: 600;
    font-size: 21px; color: var(--white); line-height: 1;
  }
  .claim-script {
    top: 764px; font-family: "Kaushan Script", cursive; font-size: 36px;
    color: var(--white); line-height: 1;
  }
  .claim-bottom {
    top: 810px; font-family: "Poppins", sans-serif; font-weight: 600;
    font-size: 21px; color: var(--white); line-height: 1;
  }
  .net-weight {
    top: 849px; font-family: "Oswald", sans-serif; font-size: 17px;
    color: var(--white); line-height: 1;
  }
</style>
</head>
<body>
<div class="canvas">

  <div class="hanger hanger--left"></div>
  <div class="hanger hanger--right"></div>

  <!-- Two colour variants share one bag structure -->
  <div class="bag bag--left">
    <svg class="bag__art" width="466" height="912" viewBox="0 0 466 912" overflow="visible">
      <defs>
        <linearGradient id="sketch-l" x1="0" x2="1">
          <stop offset="0" stop-color="#efd2a0"/><stop offset="0.2" stop-color="#f8ecc8"/>
          <stop offset="0.8" stop-color="#f8ecc8"/><stop offset="1" stop-color="#efd2a0"/>
        </linearGradient>
        <radialGradient id="panel-l" cx="0.5" cy="0.35" r="0.6">
          <stop offset="0" stop-color="var(--green-glow)"/><stop offset="1" stop-color="var(--green)"/>
        </radialGradient>
        <linearGradient id="bread-l" x1="0" y1="0" x2="0" y2="1">
          <stop offset="0" stop-color="#d89a62"/><stop offset="0.3" stop-color="#e6b080"/>
          <stop offset="0.55" stop-color="#c9844f"/><stop offset="0.8" stop-color="#e2a977"/>
          <stop offset="1" stop-color="#c07a46"/>
        </linearGradient>
        <linearGradient id="gold-l" x1="0" x2="1">
          <stop offset="0" stop-color="#d9a93a"/><stop offset="0.5" stop-color="#f7dc82"/>
          <stop offset="1" stop-color="#d9a93a"/>
        </linearGradient>
        <linearGradient id="window-l" x1="0" x2="1">
          <stop offset="0" stop-color="#fff" stop-opacity="0.55"/><stop offset="0.12" stop-color="#fff" stop-opacity="0.1"/>
          <stop offset="0.88" stop-color="#fff" stop-opacity="0.1"/><stop offset="1" stop-color="#fff" stop-opacity="0.55"/>
        </linearGradient>
      </defs>
      <rect class="bag__paper" width="466" height="420" fill="var(--cream)"/>
      <rect class="bag__sketches" role="img" aria-label="Pencil sketches of bakery goods: loaves, croissants and pretzels" width="466" height="420" fill="url(#sketch-l)"/>
      <rect class="bag__top-rule" x="13" y="27" width="437" height="5" fill="var(--gold)"/>
      <path class="bag__panel" d="M0 407 Q233 210 466 407 L466 667 L0 667 Z" fill="url(#panel-l)"/>
      <path class="bag__gold-arc" d="M-12 407 Q233 150 478 407 Q233 205 -12 407 Z" fill="url(#gold-l)"/>
      <rect class="bag__bottom-rule" x="0" y="668" width="466" height="9" fill="url(#gold-l)"/>
      <rect class="bag__bread" role="img" aria-label="Close-up photo of stacked golden bread slices" x="0" y="697" width="466" height="215" fill="url(#bread-l)"/>
      <rect class="bag__window" x="13" y="17" width="437" height="895" fill="url(#window-l)"/>
      <circle class="bag__seal" cx="393" cy="668" r="44" fill="var(--white)" stroke="var(--green)" stroke-width="5"/>
    </svg>
    <div class="bag__text brand-mark"><span class="brand-mark__dot"></span>Velorasa</div>
    <div class="bag__text brand-name">Velorasa</div>
    <div class="bag__text variant"><span class="variant__tilde">~~·</span> Cu mala de secard <span class="variant__tilde">·~~</span></div>
    <div class="bag__text claim-top">OVEN BAKED</div>
    <div class="bag__text claim-script">Fresh Bread</div>
    <div class="bag__text claim-bottom">SOFT &amp; SMOOTH</div>
    <div class="bag__text net-weight">NET WEIGHT 500G</div>
  </div>

  <div class="bag bag--right">
    <svg class="bag__art" width="466" height="912" viewBox="0 0 466 912" overflow="visible">
      <defs>
        <linearGradient id="sketch-r" x1="0" x2="1">
          <stop offset="0" stop-color="#efd2a0"/><stop offset="0.2" stop-color="#f8ecc8"/>
          <stop offset="0.8" stop-color="#f8ecc8"/><stop offset="1" stop-color="#efd2a0"/>
        </linearGradient>
        <radialGradient id="panel-r" cx="0.5" cy="0.35" r="0.6">
          <stop offset="0" stop-color="var(--crimson-glow)"/><stop offset="1" stop-color="var(--crimson)"/>
        </radialGradient>
        <linearGradient id="bread-r" x1="0" y1="0" x2="0" y2="1">
          <stop offset="0" stop-color="#d89a62"/><stop offset="0.3" stop-color="#e6b080"/>
          <stop offset="0.55" stop-color="#c9844f"/><stop offset="0.8" stop-color="#e2a977"/>
          <stop offset="1" stop-color="#c07a46"/>
        </linearGradient>
        <linearGradient id="gold-r" x1="0" x2="1">
          <stop offset="0" stop-color="#d9a93a"/><stop offset="0.5" stop-color="#f7dc82"/>
          <stop offset="1" stop-color="#d9a93a"/>
        </linearGradient>
        <linearGradient id="window-r" x1="0" x2="1">
          <stop offset="0" stop-color="#fff" stop-opacity="0.55"/><stop offset="0.12" stop-color="#fff" stop-opacity="0.1"/>
          <stop offset="0.88" stop-color="#fff" stop-opacity="0.1"/><stop offset="1" stop-color="#fff" stop-opacity="0.55"/>
        </linearGradient>
      </defs>
      <rect class="bag__paper" width="466" height="420" fill="var(--cream)"/>
      <rect class="bag__sketches" role="img" aria-label="Pencil sketches of bakery goods: loaves, croissants and pretzels" width="466" height="420" fill="url(#sketch-r)"/>
      <rect class="bag__top-rule" x="13" y="27" width="437" height="5" fill="var(--gold)"/>
      <path class="bag__panel" d="M0 407 Q233 210 466 407 L466 667 L0 667 Z" fill="url(#panel-r)"/>
      <path class="bag__gold-arc" d="M-12 407 Q233 150 478 407 Q233 205 -12 407 Z" fill="url(#gold-r)"/>
      <rect class="bag__bottom-rule" x="0" y="668" width="466" height="9" fill="url(#gold-r)"/>
      <rect class="bag__bread" role="img" aria-label="Close-up photo of stacked golden bread slices" x="0" y="697" width="466" height="215" fill="url(#bread-r)"/>
      <rect class="bag__window" x="13" y="17" width="437" height="895" fill="url(#window-r)"/>
      <circle class="bag__seal" cx="393" cy="668" r="44" fill="var(--white)" stroke="var(--green)" stroke-width="5"/>
    </svg>
    <div class="bag__text brand-mark"><span class="brand-mark__dot"></span>Velorasa</div>
    <div class="bag__text brand-name">Velorasa</div>
    <div class="bag__text variant"><span class="variant__tilde">~~·</span> Cu mala de secard <span class="variant__tilde">·~~</span></div>
    <div class="bag__text claim-top">OVEN BAKED</div>
    <div class="bag__text claim-script">Fresh Bread</div>
    <div class="bag__text claim-bottom">SOFT &amp; SMOOTH</div>
    <div class="bag__text net-weight">NET WEIGHT 500G</div>
  </div>

</div>
</body>
</html>
```